Geothermal company needs a creative "POW" business card

Manufacturers tend to be boring. We are not! We are a Geothermal Heat Pump company that has over 30 yrs of experience and wants a new look and updated feel. Nothing old (yawn) so get your creative hats on and let's rock!

We want to use the great colors of lime green and navy blue. Our new logo is attached and we're ready to roll. Remember, we're a professional leader in the geothermal industry that needs to make an eye catching and memorable first glance.

```html
<!DOCTYPE html>
<html lang="en">
<head>
<meta charset="utf-8">
<title>Tundra Loop – Business Card</title>
<link href="https://fonts.googleapis.com/css2?family=Signika:wght@300;400;600&display=swap" rel="stylesheet">
<style>
  :root {
    --bg: #efefef;
    --card: #ffffff;
    --lime: #8cc63f;
    --navy: #0d2a57;
    --forest: #2e7d32;
    --shadow: rgba(0, 0, 0, 0.12);
  }
  * { box-sizing: border-box; margin: 0; padding: 0; }
  html, body {
    width: 1200px; height: 1000px; overflow: hidden;
    background: var(--bg);
    font-family: "Signika", sans-serif;
  }
  .stage { position: relative; width: 1200px; height: 1000px; }
  .card {
    position: absolute; top: 360px; width: 496px; height: 278px;
    background: var(--card);
    box-shadow: 0 14px 40px var(--shadow);
  }
  .card--front { left: 67px; border-radius: 139px 22px 22px 139px / 139px 22px 22px 139px; }
  .card--back { left: 639px; border-radius: 22px 139px 139px 22px / 22px 139px 139px 22px; }

  .brand-name { font-weight: 600; color: var(--lime); line-height: 1; letter-spacing: -0.3px; }

  /* front */
  .front-mark { position: absolute; left: 36px; top: 33px; width: 218px; height: 218px; }
  .front-brand { position: absolute; right: 31px; top: 32px; text-align: right; }
  .front-brand .brand-name { font-size: 33px; }
  .person { position: absolute; right: 31px; top: 124px; text-align: right; }
  .person-name { font-size: 21px; font-weight: 600; color: var(--navy); line-height: 1.1; }
  .person-role { font-size: 19px; font-weight: 300; color: var(--forest); line-height: 1.35; }
  .contact { position: absolute; right: 31px; top: 198px; text-align: right;
    font-size: 14px; font-weight: 300; color: var(--lime); line-height: 18.5px; list-style: none; }

  /* back */
  .back-mark { position: absolute; left: 25px; top: 23px; width: 70px; height: 70px; }
  .back-brand { position: absolute; left: 112px; top: 38px; }
  .back-brand .brand-name { font-size: 38px; }
  .address { position: absolute; left: 26px; top: 182px; font-style: normal;
    font-size: 14px; font-weight: 300; color: var(--lime); line-height: 18.5px; }
  .website { position: absolute; left: 26px; top: 226px; font-size: 25px; font-weight: 300; color: var(--navy); }
</style>
</head>
<body>
<main class="stage">
  <section class="card card--front" aria-label="Business card front">
    <svg class="front-mark" viewBox="0 0 218 218" aria-hidden="true">
      <circle cx="109" cy="109" r="109" fill="var(--navy)"/>
    </svg>
    <div class="front-brand">
      <div class="brand-name">Tundra Loop</div>
    </div>
    <div class="person">
      <div class="person-name">Sam Ferreira</div>
      <div class="person-role">CEO</div>
    </div>
    <ul class="contact">
      <li>p: (555) 014-2200</li>
      <li>f: (555) 014-2201</li>
      <li>e: sferreira@tundraloop.com</li>
    </ul>
  </section>

  <section class="card card--back" aria-label="Business card back">
    <svg class="back-mark" viewBox="0 0 70 70" aria-hidden="true">
      <circle cx="35" cy="35" r="35" fill="var(--navy)"/>
    </svg>
    <div class="back-brand">
      <div class="brand-name">Tundra Loop</div>
    </div>
    <address class="address">18 Birch Hollow Rd<br>Lakeview, MN 56000</address>
    <div class="website">www.tundraloop.com</div>
  </section>
</main>
</body>
</html>
```